Boutique Accounting firm needs a sleek, professional facebook page.

We need a facebook page, facebook logo and a template meme/add designed that we can add text to. This page a designs need to tell the client that we are professional, approachable, understand their business needs and that they can be confident that if they work with us they will get an accountant who offers expert advice and service working with them to get the best possible outcome for their business. Our firm is located ina rural area in Gippsland VIC and deals with farmers, tradespeople, small to medium business and individuals.
attached is our logo and we want the grey used and we note that it will need to be resized to ensure it stands out and can be seen clearly.
The final design should promote growth and financial security and understanding.

Examples of pages that we identify with are:
@clearbrookledgersnz
@dunmoreassociatescharteredaccountants
@halvardenterprise

Target Market(s)

small business

Industry/Entity Type

Accounting

Colors
3176b5
0792cd

Requirements
Must have
• our logo must be designed so that the words of our brand fill up the area
Nice to have
• .
Should not have
• .

```html
<!DOCTYPE html>
<html lang="en">
<head>
<meta charset="utf-8">
<title>Hollis Brandt – Facebook Page Set</title>
<link rel="stylesheet" href="https://fonts.googleapis.com/css2?family=Tinos:wght@400;700&display=swap">
<style>
  :root {
    --brand-blue: #0b8fcf;
    --deep-blue: #3176b5;
    --brand-grey: #58595b;
    --paper: #ffffff;
  }
  html, body {
    margin: 0;
    padding: 0;
    width: 1200px;
    height: 2571px;
    overflow: hidden;
    background: var(--paper);
    font-family: "Tinos", "Times New Roman", serif;
  }
  .canvas {
    position: relative;
    width: 1200px;
    height: 2571px;
    overflow: hidden;
    background: var(--paper);
  }
  .cover-banner {
    position: absolute;
    left: 55px;
    top: 80px;
    width: 1110px;
    height: 417px;
    box-shadow: 0 4px 10px rgba(0,0,0,0.18);
  }
  .showcase-band {
    position: absolute;
    left: 0;
    top: 566px;
    width: 1200px;
    height: 800px;
    background: var(--brand-blue);
    overflow: hidden;
  }
  .post-tile {
    position: absolute;
    width: 558px;
    height: 554px;
    box-shadow: 0 4px 10px rgba(0,0,0,0.18);
  }
  .post-tile--team      { left: 33px;  top: 1409px; }
  .post-tile--call      { left: 614px; top: 1409px; }
  .post-tile--profile   { left: 33px;  top: 1985px; }
  .post-tile--group     { left: 614px; top: 1985px; }
  svg text { font-family: "Tinos", "Times New Roman", serif; }
  .headline { font-weight: 700; fill: var(--paper); }
  .subline  { font-weight: 400; fill: var(--paper); }
  .brand-name { font-weight: 700; fill: var(--brand-grey); }
  .brand-name--blue { fill: var(--brand-blue); }
</style>
</head>
<body>
<main class="canvas">

  <!-- Cover banner -->
  <svg class="cover-banner" viewBox="0 0 1110 417" xmlns="http://www.w3.org/2000/svg">
    <defs>
      <linearGradient id="officeTone" x1="0" y1="0" x2="1" y2="1">
        <stop offset="0" stop-color="#eef3f8"/>
        <stop offset="0.55" stop-color="#b8c3ce"/>
        <stop offset="1" stop-color="#4d5966"/>
      </linearGradient>
      <clipPath id="bannerClip"><rect width="1110" height="417"/></clipPath>
    </defs>
    <g clip-path="url(#bannerClip)">
      <rect x="300" y="0" width="810" height="417" fill="url(#officeTone)" role="img" aria-label="Photo of a cheering business team with raised arms in a bright office"/>
      <circle class="cover-circle" cx="70" cy="205" r="343" fill="var(--brand-blue)"/>
      <rect class="cover-frame" x="314" y="26" width="771" height="360" fill="none" stroke="var(--brand-blue)" stroke-width="4"/>
      <text class="headline" x="38" y="132" font-size="62">Business</text>
      <text class="subline" x="40" y="177" font-size="34">works like</text>
      <text class="subline" x="40" y="216" font-size="34">a magic.</text>
      <circle class="logo-disc" cx="128" cy="411" r="155" fill="var(--paper)"/>
      <text class="brand-name" x="42" y="345" font-size="26">Hollis Brandt</text>
      <text x="44" y="368" font-size="11" fill="var(--brand-grey)" letter-spacing="1">ACCOUNTANTS &amp; ADVISORS</text>
    </g>
  </svg>

  <!-- Profile picture showcase -->
  <section class="showcase-band">
    <svg width="1200" height="800" viewBox="0 0 1200 800" xmlns="http://www.w3.org/2000/svg">
      <circle cx="951" cy="188" r="137" fill="var(--paper)"/>
      <circle cx="955" cy="625" r="103" fill="var(--paper)"/>
      <rect x="125" y="300" width="124" height="228" fill="none" stroke="var(--paper)" stroke-width="6"/>
      <g class="profile-picture">
        <rect x="410" y="210" width="380" height="380" fill="var(--paper)"/>
        <rect x="450" y="250" width="300" height="300" fill="none" stroke="var(--brand-blue)" stroke-width="8"/>
        <text class="brand-name brand-name--blue" x="600" y="412" font-size="40" text-anchor="middle">Hollis Brandt</text>
      </g>
    </svg>
  </section>

  <!-- Post: team at work -->
  <svg class="post-tile post-tile--team" viewBox="0 0 558 554" xmlns="http://www.w3.org/2000/svg">
    <defs>
      <linearGradient id="teamTone" x1="0" y1="0" x2="1" y2="1">
        <stop offset="0" stop-color="#f2f5f8"/>
        <stop offset="0.5" stop-color="#c7b8aa"/>
        <stop offset="1" stop-color="#5a4f48"/>
      </linearGradient>
      <clipPath id="teamClip"><rect width="558" height="554"/></clipPath>
    </defs>
    <g clip-path="url(#teamClip)">
      <rect width="558" height="554" fill="url(#teamTone)" role="img" aria-label="Photo of a young team gathered around a table working together"/>
      <circle cx="293" cy="768" r="403" fill="var(--brand-blue)"/>
      <rect x="22" y="14" width="518" height="514" fill="none" stroke="var(--brand-blue)" stroke-width="3"/>
      <path d="M0 0 H190 V33 A32 32 0 0 1 158 65 H0 Z" fill="var(--paper)"/>
      <text class="brand-name" x="20" y="38" font-size="22">Hollis Brandt</text>
      <text class="headline" x="276" y="451" font-size="41" text-anchor="middle">Lorem ipsum</text>
      <text class="subline" x="276" y="477" font-size="20" text-anchor="middle">dolor sit amet, no latine</text>
      <text class="subline" x="276" y="497" font-size="20" text-anchor="middle">explicari pri, no mei</text>
      <text class="subline" x="276" y="518" font-size="20" text-anchor="middle">partiendo adversarium, ei</text>
    </g>
  </svg>

  <!-- Post: call to action -->
  <svg class="post-tile post-tile--call" viewBox="0 0 558 554" xmlns="http://www.w3.org/2000/svg">
    <defs>
      <linearGradient id="callTone" x1="0" y1="0" x2="1" y2="0">
        <stop offset="0" stop-color="#d6e2ea"/>
        <stop offset="0.6" stop-color="#e8edf1"/>
        <stop offset="1" stop-color="#a9b6c2"/>
      </linearGradient>
      <clipPath id="callClip"><rect width="558" height="554"/></clipPath>
    </defs>
    <g clip-path="url(#callClip)">
      <rect width="558" height="554" fill="url(#callTone)" role="img" aria-label="Photo of a smiling support agent wearing a headset"/>
      <circle cx="100" cy="650" r="410" fill="var(--brand-blue)"/>
      <rect x="22" y="14" width="514" height="514" fill="none" stroke="var(--brand-blue)" stroke-width="3"/>
      <path d="M0 0 H190 V33 A32 32 0 0 1 158 65 H0 Z" fill="var(--paper)"/>
      <text class="brand-name" x="20" y="38" font-size="22">Hollis Brandt</text>
      <text class="headline" x="27" y="398" font-size="58">Give us</text>
      <text class="headline" x="27" y="459" font-size="58">a call today.</text>
      <text class="subline" x="29" y="490" font-size="20">Lorem ipsum dolor sit amet, no latine</text>
      <text class="subline" x="29" y="511" font-size="20">explicari pri, no mei partiendo adversarium</text>
    </g>
  </svg>

  <!-- Post: team member profile -->
  <svg class="post-tile post-tile--profile" viewBox="0 0 558 554" xmlns="http://www.w3.org/2000/svg">
    <defs>
      <linearGradient id="memberTone" x1="0" y1="0" x2="0" y2="1">
        <stop offset="0" stop-color="#eef1f4"/>
        <stop offset="0.45" stop-color="#c9b6a6"/>
        <stop offset="1" stop-color="#23272d"/>
      </linearGradient>
      <clipPath id="profileClip"><rect width="558" height="554"/></clipPath>
    </defs>
    <g clip-path="url(#profileClip)">
      <rect width="558" height="554" fill="var(--brand-blue)"/>
      <circle cx="578" cy="330" r="320" fill="url(#memberTone)" role="img" aria-label="Portrait photo of a smiling team member in a dark suit"/>
      <path d="M0 0 H190 V33 A32 32 0 0 1 158 65 H0 Z" fill="var(--paper)"/>
      <text class="brand-name" x="20" y="38" font-size="22">Hollis Brandt</text>
      <text class="headline" x="29" y="231" font-size="26">OWEN PRICE</text>
      <text class="subline" x="29" y="259" font-size="20">Digital Marketing</text>
      <rect x="29" y="270" width="166" height="2" fill="var(--paper)"/>
      <text class="subline" x="29" y="305" font-size="19">dolor sit amet, no latine</text>
      <text class="subline" x="29" y="325" font-size="19">explicari pri, no mei</text>
      <text class="subline" x="29" y="345" font-size="19">partiendo adversarium, ei</text>
    </g>
  </svg>

  <!-- Post: group message -->
  <svg class="post-tile post-tile--group" viewBox="0 0 558 554" xmlns="http://www.w3.org/2000/svg">
    <defs>
      <linearGradient id="groupTone" x1="0" y1="0" x2="0" y2="1">
        <stop offset="0" stop-color="#eef2f5"/>
        <stop offset="0.4" stop-color="#c4b2a3"/>
        <stop offset="1" stop-color="#2a2f36"/>
      </linearGradient>
      <clipPath id="groupClip"><rect width="558" height="554"/></clipPath>
    </defs>
    <g clip-path="url(#groupClip)">
      <rect width="558" height="554" fill="var(--brand-blue)"/>
      <circle cx="283" cy="566" r="352" fill="url(#groupTone)" role="img" aria-label="Photo of four smiling colleagues in business suits"/>
      <path d="M0 0 H190 V33 A32 32 0 0 1 158 65 H0 Z" fill="var(--paper)"/>
      <text class="brand-name" x="20" y="38" font-size="22">Hollis Brandt</text>
      <text class="headline" x="261" y="77" font-size="41">Lorem ipsum</text>
      <text class="subline" x="261" y="111" font-size="20">dolor sit amet, no latine</text>
      <text class="subline" x="261" y="132" font-size="20">explicari pri, no mei</text>
      <text class="subline" x="261" y="152" font-size="20">partiendo adversarium, ei</text>
    </g>
  </svg>

</main>
</body>
</html>
```